Marrow Business Cards

Front of business card will have logo, name, address, & telephone number. Back of card will have a list of services provided - Roads, Substation Pads, Temporary Pads, Site Pads, Land Leveling, Powerline Row Cleaning, Land Clearing, Gates, Fencing, Construction Entrances, Excavation, Trenching, Underground Utilities, Directional Boring, Pile Driving. We are a construction company that uses heavy equipment like bulldozers, motor graders/blades, dump trucks, backhoes, hydro axes, & skid loaders. We build roads, pads, & install electric utility lines & waterlines underground. This logo is new. The word "Construction" can be smaller as uploaded 2 example edited logos. We will be using this card design for many employees.
Target Market(s)
Industrial Electric Powerline, Wind Turbine, Solar Panel, & Water Utility companies.
Contact Information for Business Card
Name/Position - Dorian Quale - Owner
Address: 4837 FM 582
Merkel, TX 79418
Phone number - (325) 418-2906

```html
<!DOCTYPE html>
<html lang="en">
<head>
<meta charset="utf-8">
<title>Marrow Construction – Business Cards</title>
<link rel="stylesheet" href="https://fonts.googleapis.com/css2?family=Roboto:wght@400;500;700&display=swap">
<style>
  :root {
    --page-bg: #e4e2e0;
    --card-maroon: #3d111b;
    --card-maroon-light: #4d1d27;
    --ink-white: #ffffff;
    --card-shadow: rgba(0, 0, 0, 0.28);
  }
  * { box-sizing: border-box; margin: 0; padding: 0; }
  html, body {
    width: 1200px;
    height: 900px;
    overflow: hidden;
    background: var(--page-bg);
    font-family: "Roboto", Arial, sans-serif;
    color: var(--ink-white);
  }
  .canvas {
    position: relative;
    width: 1200px;
    height: 900px;
  }
  .card {
    position: absolute;
    left: 250px;
    width: 700px;
    height: 400px;
    background: linear-gradient(100deg, var(--card-maroon-light) 0%, var(--card-maroon) 28%, var(--card-maroon) 100%);
    box-shadow: 0 10px 24px var(--card-shadow);
  }
  .card--services { top: 40px; }
  .card--contact { top: 470px; }

  /* Services side */
  .wordmark {
    font-weight: 500;
    color: var(--ink-white);
    text-transform: uppercase;
    line-height: 1;
  }
  .card--services .wordmark {
    position: absolute;
    top: 110px;
    left: 0;
    width: 100%;
    text-align: center;
    font-size: 64px;
    letter-spacing: 4px;
  }
  .services-list {
    position: absolute;
    top: 232px;
    left: 40px;
    right: 40px;
    text-align: center;
    font-size: 15px;
    line-height: 1.55;
    letter-spacing: 0.2px;
  }
  .services-list .sep { padding: 0 5px; }

  /* Contact side */
  .card--contact .logo-block {
    position: absolute;
    top: 48px;
    right: 48px;
    text-align: right;
  }
  .card--contact .wordmark--name {
    font-size: 48px;
    letter-spacing: 4px;
  }
  .card--contact .wordmark--tag {
    margin-top: 10px;
    font-size: 30px;
    letter-spacing: 3px;
  }
  .contact {
    position: absolute;
    left: 48px;
    bottom: 40px;
  }
  .contact__name {
    font-size: 24px;
    font-weight: 700;
    text-transform: uppercase;
    letter-spacing: 0.5px;
  }
  .contact__role {
    font-size: 19px;
    font-weight: 400;
    margin-top: 2px;
  }
  .contact__rule {
    width: 22px;
    height: 1.5px;
    background: var(--ink-white);
    margin: 14px 0 12px 14px;
  }
  .contact__line {
    display: flex;
    align-items: center;
    gap: 10px;
    font-size: 20px;
    margin-left: 14px;
    margin-top: 6px;
  }
  .contact__line svg { width: 16px; height: 16px; flex: none; }
</style>
</head>
<body>
<main class="canvas">

  <section class="card card--services" aria-label="Business card, services side">
    <div class="wordmark">Marrow</div>
    <p class="services-list">
      Roads<span class="sep">I</span>Substation Pads<span class="sep">I</span>Temporary Pads<span class="sep">I</span>Site Pads<span class="sep">I</span>Land Leveling<br>
      Land Clearing<span class="sep">I</span>Gates<span class="sep">I</span>Fencing<span class="sep">I</span>Construction Entrances<span class="sep">I</span>Excavation<span class="sep">I</span>Trenching<br>
      Underground Utilities<span class="sep">I</span>Powerline Row Cleaning<span class="sep">I</span>Pile Driving<span class="sep">I</span>Directional Boring
    </p>
  </section>

  <section class="card card--contact" aria-label="Business card, contact side">
    <div class="logo-block">
      <div class="wordmark wordmark--name">Marrow</div>
      <div class="wordmark wordmark--tag">Construction</div>
    </div>

    <div class="contact">
      <div class="contact__name">Dorian Quale</div>
      <div class="contact__role">Owner</div>
      <div class="contact__rule"></div>
      <div class="contact__line">
        <svg viewBox="0 0 24 24" aria-hidden="true"><path fill="#fff" d="M6.6 10.8a15.1 15.1 0 0 0 6.6 6.6l2.2-2.2a1 1 0 0 1 1-.25 11.4 11.4 0 0 0 3.6.57 1 1 0 0 1 1 1V20a1 1 0 0 1-1 1A17 17 0 0 1 3 4a1 1 0 0 1 1-1h3.5a1 1 0 0 1 1 1c0 1.25.2 2.45.57 3.57a1 1 0 0 1-.25 1z"/></svg>
        <span>(325) 418-2906</span>
      </div>
      <div class="contact__line">
        <svg viewBox="0 0 24 24" aria-hidden="true"><path fill="#fff" d="M12 2a7 7 0 0 0-7 7c0 5.25 7 13 7 13s7-7.75 7-13a7 7 0 0 0-7-7zm0 9.5A2.5 2.5 0 1 1 12 6.5a2.5 2.5 0 0 1 0 5z"/></svg>
        <span>4837 FM 582 Merkel, TX 79418</span>
      </div>
    </div>
  </section>

</main>
</body>
</html>
```